Business Cards for a start up company

We are looking for a business card design for a start up company based in Ohio. The logo is attached. We are a healthcare company. We are open to all designs but want something professional but fun; creative, not boring

Industry/Entity Type

Healthcare

```html
<!DOCTYPE html>
<html lang="en">
<head>
<meta charset="utf-8">
<title>Bright Path Care – Business Card</title>
<link rel="stylesheet" href="https://fonts.googleapis.com/css2?family=Playfair+Display:wght@400&family=Arimo:wght@400&display=swap">
<style>
  :root {
    --backdrop: #e9e6e1;
    --card-white: #ffffff;
    --navy: #1f1f72;
    --navy-deep: #14145a;
    --silver: #d9dbe3;
    --ink: #2a2a7a;
    --web-text: #ffffff;
  }
  html, body {
    margin: 0;
    padding: 0;
    width: 1200px;
    height: 900px;
    overflow: hidden;
    background: var(--backdrop);
  }
  .stage {
    position: relative;
    width: 1200px;
    height: 900px;
  }
  .business-card {
    position: absolute;
    left: 160px;
    top: 200px;
    width: 880px;
    height: 500px;
    background: var(--card-white);
    overflow: hidden;
    box-shadow: 0 18px 40px rgba(0, 0, 0, 0.18);
  }
  .card-swoosh {
    position: absolute;
    inset: 0;
    width: 880px;
    height: 500px;
  }
  .brand {
    position: absolute;
    left: 120px;
    top: 170px;
    display: flex;
    align-items: center;
    gap: 26px;
  }
  .brand-dot {
    width: 64px;
    height: 64px;
    border-radius: 50%;
    background: var(--navy);
  }
  .brand-name {
    font-family: "Playfair Display", Georgia, serif;
    font-weight: 400;
    font-size: 64px;
    color: var(--ink);
    letter-spacing: 0.5px;
    margin: 0;
  }
  .web-address {
    position: absolute;
    right: 70px;
    bottom: 58px;
    font-family: "Arimo", Arial, sans-serif;
    font-size: 24px;
    color: var(--web-text);
    letter-spacing: 0.6px;
    margin: 0;
  }
</style>
</head>
<body>
  <main class="stage">
    <section class="business-card" aria-label="Business card front">
      <svg class="card-swoosh" viewBox="0 0 880 500" aria-hidden="true">
        <defs>
          <linearGradient id="navy-fade" x1="0" y1="0" x2="1" y2="1">
            <stop offset="0" stop-color="#2a2a86"/>
            <stop offset="1" stop-color="#14145a"/>
          </linearGradient>
          <linearGradient id="silver-fade" x1="0" y1="0" x2="1" y2="0">
            <stop offset="0" stop-color="#ffffff"/>
            <stop offset="1" stop-color="#d4d6df"/>
          </linearGradient>
        </defs>
        <path d="M0 500 L0 430 C 260 400, 620 300, 880 40 L880 500 Z" fill="url(#silver-fade)"/>
        <path d="M0 500 L0 470 C 280 440, 660 330, 880 90 L880 500 Z" fill="url(#navy-fade)"/>
        <path d="M0 470 C 280 440, 660 330, 880 90" fill="none" stroke="#ffffff" stroke-opacity="0.7" stroke-width="3"/>
      </svg>
      <div class="brand">
        <span class="brand-dot"></span>
        <h1 class="brand-name">Bright Path Care</h1>
      </div>
      <p class="web-address">www.brightpathcare.com</p>
    </section>
  </main>
</body>
</html>
```